UK Supplement Company Needs a Label for Diet Protein Powder

We need a new, modern and fresh design for our Diet Protein Powder. Our protein powder is packaged in black plastic tubs (photo attached) and needs an attractive label. We would like to see designs that grab attention and look professional. We're very open to ideas. The label should be 88mm x 365mm. We also prefer PSD format where possible. These alterations could be made once your design is chosen. Have attached photo of our shake ingredients/benefits.
Updates

Need extra days to review

Target Market(s)

Slimmers

Industry/Entity Type

Health And Wellness

Font styles to use
Serif
Sans Serif

Colors

Designer to choose colors to be used in the design.

Requirements
Must have
• Clean, Modern and Professional Look. Eye catching. The flavour, we offer 6 flavours so this must be something we can edit (Flavours are Banana, Chocolate, Chocolate Mint, Strawberry, Toffee and Vanilla).
Nice to have
• Our logo, this can be BRISK Nutrition or just BRISK. Our logo files are attached.
Should not have
• We do not want to see people (faces or bodies) on the design.

```html
<!DOCTYPE html>
<html lang="en">
<head>
<meta charset="utf-8">
<title>BRISK Nutrition – Low Calorie Protein Shake Label</title>
<link href="https://fonts.googleapis.com/css2?family=Montserrat:wght@300;400;500;600;700&family=Arimo:wght@400;700&display=swap" rel="stylesheet">
<style>
  :root {
    --backdrop: #b4b4b4;
    --paper: #ffffff;
    --brand-red: #c2373d;
    --swoosh-red: #ee3b52;
    --swoosh-pink: #f7a3b0;
    --ink: #2b2b2b;
    --muted: #555555;
    --green-1: #4cb97a;
    --green-2: #2ea15c;
    --green-3: #1f8a45;
    --green-4: #13773a;
  }
  * { box-sizing: border-box; margin: 0; padding: 0; }
  html, body { width: 1008px; height: 1200px; overflow: hidden; }
  body {
    background: var(--backdrop);
    font-family: 'Montserrat', sans-serif;
    color: var(--ink);
    position: relative;
  }
  .label {
    position: absolute;
    left: 24px; top: 484px;
    width: 960px; height: 231px;
    background: var(--paper);
    box-shadow: 0 18px 40px rgba(0,0,0,0.25);
    overflow: hidden;
  }
  .label > * { position: absolute; }

  /* Nutrition facts panel */
  .nutrition {
    left: 25px; top: 19px; width: 267px; height: 75px;
    border: 1px solid #999; padding: 3px 4px;
    font-family: 'Arimo', sans-serif; color: #111;
    display: flex; gap: 6px;
  }
  .nutrition .intro { width: 76px; font-size: 4.6px; line-height: 1.25; }
  .nutrition .intro h3 { font-size: 12.5px; line-height: 1.05; font-weight: 700; margin-bottom: 2px; }
  .nutrition table { border-collapse: collapse; font-size: 4.6px; flex: 1; align-self: flex-start; }
  .nutrition td { padding: 1px 1px; border-bottom: 0.5px solid #777; white-space: nowrap; }
  .nutrition thead td { border-bottom: 2px solid #111; font-size: 3.6px; }
  .nutrition .pct { text-align: right; }
  .nutrition .indent { padding-left: 7px; }
  .nutrition b { font-weight: 700; }

  .caution { left: 23px; top: 126px; width: 268px; }
  .caution h4 { font-size: 8.5px; font-weight: 500; margin-bottom: 5px; }
  .caution p { font-size: 5.6px; line-height: 1.6; color: var(--muted); font-weight: 300; }
  .maker { left: 10px; top: 214px; font-size: 5.4px; color: var(--muted); }

  /* Centre panel */
  .brand-tab {
    left: 412px; top: 0; width: 131px; height: 61px;
    background: var(--brand-red);
    border-radius: 0 0 6px 6px;
    color: #fff; text-align: center; padding-top: 12px;
  }
  .brand-tab .name { font-size: 27px; font-weight: 700; line-height: 1; letter-spacing: -0.5px; }
  .brand-tab .tag { font-size: 5.4px; letter-spacing: 3.6px; font-weight: 600; margin-top: 3px; }
  .centre-line { left: 0; width: 954px; text-align: center; font-weight: 300; }
  .dietary { top: 68px; font-size: 13.5px; letter-spacing: 0.3px; left: 0; }
  .rule { left: 356px; top: 92px; width: 242px; height: 1px; background: var(--brand-red); }
  .law { top: 98px; font-size: 15px; letter-spacing: 0.6px; }
  .shake { top: 121px; font-size: 15px; letter-spacing: 0.6px; font-weight: 400; }
  .shake .pill {
    background: var(--brand-red); color: #fff; font-weight: 600;
    padding: 0 2px; border-radius: 3px;
  }
  .stat { text-align: center; font-size: 8.5px; font-weight: 400; line-height: 1; }
  .stat small { display: block; font-size: 3.8px; letter-spacing: 0.6px; margin-top: 2px; color: var(--muted); }
  .stat.cal { left: 354px; top: 151px; }
  .stat.carb { left: 541px; top: 151px; }
  .fruit {
    left: 451px; top: 154px; width: 44px; height: 27px;
    border-radius: 45% 45% 50% 50%;
    background: radial-gradient(circle at 40% 55%, #e0262f 0%, #b3171e 65%, #5c8f2e 100%);
  }
  .flavour { left: 0; width: 954px; top: 178px; text-align: center; }
  .flavour .f-name { font-size: 8.4px; font-weight: 700; color: var(--brand-red); letter-spacing: 0.3px; }
  .flavour .f-sub { font-size: 3.8px; color: var(--muted); letter-spacing: 0.8px; }
  .swoosh { left: 316px; top: 186px; width: 322px; height: 45px; }
  .badges { left: 347px; top: 196px; display: flex; gap: 2px; }
  .badge {
    width: 23px; height: 21px; color: #fff; text-align: center;
    font-size: 5px; font-weight: 700; padding-top: 3px; line-height: 1;
  }
  .badge small { display: block; font-size: 2.6px; font-weight: 500; margin-top: 1.5px; }
  .badge:nth-child(1) { background: var(--green-1); }
  .badge:nth-child(2) { background: var(--green-2); font-size: 8px; padding-top: 2px; }
  .badge:nth-child(3) { background: var(--green-3); }
  .badge:nth-child(4) { background: var(--green-4); }

  /* Right panel */
  .info { right: 17px; width: 262px; text-align: right; }
  .info h4 { font-size: 8.5px; font-weight: 500; margin-bottom: 13px; }
  .info p { font-size: 5.6px; line-height: 1.6; color: var(--muted); font-weight: 300; }
  .info.use { top: 37px; }
  .info.ingredients { top: 99px; }
  .info.ingredients h4 { margin-bottom: 9px; }
  .info.allergens { top: 161px; }
  .info.allergens h4 { margin-bottom: 5px; }
</style>
</head>
<body>
<main class="label">
  <section class="nutrition">
    <div class="intro">
      <h3>Nutrition Facts</h3>
      <div>Serving Size 2 turtles (38g)</div>
      <div>Servings Per Container 6</div>
      <div><b>Calories</b> 220</div>
      <div style="padding-left:6px">Calories from Fat 180</div>
      <div style="font-size:3.4px;margin-top:2px">*Percent Daily Values are based on a 2,000 calorie diet</div>
    </div>
    <table>
      <thead><tr><td>Amount / Serving</td><td class="pct">% Daily Value*</td><td>Amount / Serving</td><td class="pct">% Daily Value*</td></tr></thead>
      <tbody>
        <tr><td><b>Total Fat</b> 18g</td><td class="pct">28%</td><td><b>Total Carbohydrate</b> 16g</td><td class="pct">5%</td></tr>
        <tr><td class="indent">Saturated Fat 4g</td><td class="pct">20%</td><td class="indent">Dietary Fiber 2g</td><td class="pct">8%</td></tr>
        <tr><td class="indent">Trans Fat 0g</td><td></td><td class="indent">Sugars 11g</td><td></td></tr>
        <tr><td><b>Cholesterol</b> 5mg</td><td class="pct">2%</td><td><b>Protein</b> 2g</td><td></td></tr>
        <tr><td><b>Sodium</b> 20mg</td><td class="pct">1%</td><td></td><td></td></tr>
        <tr><td>Vitamin A 2% &nbsp;•</td><td>Vitamin C 0%</td><td>Calcium 4% &nbsp;•</td><td>Iron 4%</td></tr>
      </tbody>
    </table>
  </section>

  <section class="caution">
    <h4>CAUTION:</h4>
    <p>This product should not be used as a substitud for a balanced and healthy lifestyle. Not recomended for use by pregnant or lectatingwomen. If you are taking any medications or under medical suprevission, you should consult with your GP before use. Not intended for use by persons under the age of 18. Not intended for long term usage</p>
  </section>
  <p class="maker">Manufactured in the uk for brisk nutrition limited, mill lane, north ashby, ab12 3cd.</p>

  <div class="brand-tab">
    <div class="name">BRISK</div>
    <div class="tag">NUTRITION</div>
  </div>
  <h2 class="centre-line dietary">DIETARY SUPPLEMENT</h2>
  <div class="rule"></div>
  <h1 class="centre-line law">LAW CALORIE</h1>
  <h1 class="centre-line shake"><span class="pill">PROTIEN</span> SHAKE</h1>
  <div class="stat cal">117 CALORIES<small>PER SERVING</small></div>
  <div class="stat carb">4.2 CARBS<small>PER SERVING</small></div>
  <div class="fruit" role="img" aria-label="Strawberries illustration"></div>
  <div class="flavour"><div class="f-name">STRAWBERRY</div><div class="f-sub">FLAVOUR</div></div>

  <svg class="swoosh" viewBox="0 0 322 45" preserveAspectRatio="none" aria-hidden="true">
    <path d="M0 45 C110 40 200 18 322 0 L322 45 Z" fill="var(--swoosh-pink)"/>
    <path d="M20 45 C130 38 230 10 322 4 L322 45 Z" fill="var(--swoosh-red)"/>
  </svg>
  <div class="badges">
    <div class="badge">120 MG<small>GREEN TEA EXTRACT</small></div>
    <div class="badge">21G<small>PROTIEN</small></div>
    <div class="badge">120 MG<small>ACAI BERRY</small></div>
    <div class="badge">15 MG<small>CLR POWDER</small></div>
  </div>

  <section class="info use">
    <h4>SUGGESTED USE:</h4>
    <p>Mix one level scoop (30g) with at least 200ml of cold water or skimmed milk in a shaker. reseal pouch after each use. store in cool and dry place. Keep away from children.</p>
  </section>
  <section class="info ingredients">
    <h4>INGREDIENTS:</h4>
    <p>protein Blend (soys protein Isolate, Whey protein concentrate (MILK), MILK PROTEIN), Acety-L-Carnitine, Acai Berry Extract, Green Tea Extract, CLA Powder, Flavourings, Colorings, Xanthan Gum, Sweetener: Sucralose.</p>
  </section>
  <section class="info allergens">
    <h4>ALLERGENS:</h4>
    <p>for alergers, see ingredients in bold, Processed on equipment which also processes gluten, nuts egg and peanuts</p>
  </section>
</main>
</body>
</html>
```